Wordpress Design Project (Bramblewick)

We need a wordpress design for an established auction and real estate company based in New Hampshire. The winning design will incorporate the colors of logo (red and blue) creatively with black or gray in a very professional and clean layout. Client mentions liking the site http://www.veltranbids.com/ as a general idea.

Industry/Entity Type

Real Estate

Requirements
Must have
• Navigation:
1) Home (lorem text)
2) Upcoming Auctions
3) Auction Results
4) Sell or Consign
5) About Us
6) Services
7) FAQ
8) Contact Us

Site will have slideshow, initial image attached.
Sidebar widgets:
- Email sign up form
- Featured Auction (like at http://www.dorvexsalehouse.com) - - - - Video Widget
- Testimonials widget

Footer will have smaller logo, contact info, and 2 association logos (attached)
-
Nice to have
• use of drop-down menu design for 'Services'
1) Appraisals
2) Consulting
Should not have
• please use no gavels in the design

```html
<!DOCTYPE html>
<html lang="en">
<head>
<meta charset="utf-8">
<title>Bramblewick Auctioneers</title>
<link href="https://fonts.googleapis.com/css2?family=Ubuntu:wght@500;700&family=Arimo:ital,wght@0,400;0,700;1,400&display=swap" rel="stylesheet">
<style>
:root{
  --navy:#1c2a6b;
  --navy-dark:#121c50;
  --red:#9b1a1e;
  --red-bright:#c4262b;
  --text:#333;
  --muted:#555;
  --panel:#f4f4f4;
  --footer:#3b3b3b;
  --footer-dark:#2c2c2c;
}
*{box-sizing:border-box;margin:0;padding:0}
html,body{width:960px;height:1200px;overflow:hidden;background:#fff;font-family:Arimo,Arial,sans-serif;color:var(--text)}
.page{position:relative;width:960px;height:1200px;overflow:hidden}
.abs{position:absolute}
.top-band{left:0;top:40px;width:960px;height:402px;background:linear-gradient(#f7f7f7,#ececec 80%,#e4e4e4)}
.nav{left:0;top:0;width:960px;height:40px;background:linear-gradient(#2b3a86,#1c2a6b);border-top:5px solid var(--red)}
.nav a{position:absolute;top:10px;transform:translateX(-50%);color:#fff;text-decoration:none;font-family:Ubuntu,sans-serif;font-weight:500;font-size:11.5px;white-space:nowrap}
.nav .active{top:6px;padding:5px 12px;background:var(--red);border:1px solid #6d0f12;border-radius:3px;box-shadow:inset 0 1px 0 #c54}
.dropdown{left:322px;top:42px;width:136px;height:54px;background:#444;border:1px solid #666;padding:6px 5px}
.dropdown:before{content:"";position:absolute;left:26px;top:-7px;border:6px solid transparent;border-bottom-color:#444;border-top:0}
.dropdown div{font-size:9.5px;color:#fff;padding:3px 5px;height:18px}
.dropdown .on{background:var(--red)}
.brand{left:86px;top:58px;display:flex;align-items:center;gap:8px}
.brand-mark{width:58px;height:58px;border-radius:50%;background:var(--navy)}
.brand-name{font-family:Ubuntu,sans-serif;font-weight:500;font-size:22px;color:var(--navy);letter-spacing:1px}
.phone{left:718px;top:101px;display:flex;align-items:center;gap:7px;font-family:Ubuntu,sans-serif;font-weight:700;font-size:19px;color:#111}
.phone-icon{width:20px;height:20px;background:var(--red);border-radius:3px;display:flex;align-items:center;justify-content:center}
.frame{left:80px;top:136px;width:797px;height:380px;background:#fff;box-shadow:0 0 4px rgba(0,0,0,.15)}
.slide{left:86px;top:142px;width:524px;height:354px;background:radial-gradient(circle at 45% 45%,#d8d4c8,#a59d8c 60%,#6d6253)}
.signup{left:610px;top:142px;width:260px;height:354px;background:linear-gradient(135deg,#2d3d8d,#1a2566);padding:18px 22px 0 22px;color:#fff}
.signup h2{font-family:Ubuntu,sans-serif;font-weight:500;font-size:19px;margin-bottom:12px}
.signup p{font-size:9.8px;line-height:14px;margin-left:3px;margin-bottom:10px}
.field{width:202px;height:36px;border-radius:18px;background:linear-gradient(#fff,#e8e8e8);border:2px solid #d6d6d6;font-size:10px;color:#444;padding:11px 17px;margin-bottom:12px}
.subscribe{margin-left:80px;width:122px;height:37px;border-radius:10px;background:linear-gradient(#d33,#a3161b);border:2px solid #e06;border-color:#e45a5a;font-family:Ubuntu,sans-serif;font-weight:700;font-size:13.5px;color:#fff;text-align:center;line-height:33px}
.arc{left:0;top:440px}
.welcome{left:0;top:482px;width:960px;display:flex;justify-content:center;align-items:center;gap:6px;font-family:Ubuntu,sans-serif;font-weight:500;font-size:19px;color:var(--navy)}
.welcome .dot{width:34px;height:34px;border-radius:50%;background:var(--navy)}
.welcome .name{color:var(--red)}
.intro{left:102px;top:537px;width:756px;text-align:center;font-size:10.5px;line-height:16px;color:#444}
.divider{left:100px;top:655px;width:760px;height:3px;background:radial-gradient(ellipse at center,#d6d6d6,transparent 75%)}
.head{height:34px;background:linear-gradient(#2a3a88,#15205a);border-radius:6px 6px 0 0;color:#fff;font-family:Ubuntu,sans-serif;font-weight:500;font-size:15px;line-height:34px}
.listings{left:92px;top:680px;width:542px}
.listings .head{padding-left:16px}
.row{position:relative;height:110px;border-bottom:1px dashed #ccc}
.row.alt{background:var(--panel)}
.thumb{position:absolute;left:10px;top:21px;width:111px;height:74px;border:2px solid #d0d0d0}
.info{position:absolute;left:132px;top:20px;font-size:9.5px;line-height:11.5px;font-style:italic;color:#333}
.info .title{color:var(--red);font-size:11px;margin-bottom:5px}
.info b{font-weight:700}
.btns{position:absolute;left:439px;top:27px;width:90px}
.btn{height:25px;border-radius:5px;color:#fff;font-family:Ubuntu,sans-serif;font-weight:500;font-size:11px;display:flex;align-items:center;gap:10px;padding-left:15px;border:1px solid #ddd}
.btn.red{background:linear-gradient(#d22b30,#a0161b)}
.btn.blue{background:linear-gradient(#2a3a88,#15205a);margin-top:1px}
.btn i{width:11px;height:12px;background:#dfe6f0;border-radius:1px;display:block}
.side{left:666px;width:204px}
.side .head{text-align:center}
.featured-img{margin:18px 0 0 5px;width:187px;height:78px;background:linear-gradient(120deg,#8a8a8a,#cbb77a 45%,#6b3b2a 80%);box-shadow:0 0 3px rgba(0,0,0,.3)}
.feat-link{margin:9px 0 0 13px;font-size:10px;color:var(--navy);text-decoration:underline;letter-spacing:.5px}
.feat-text{margin:6px 0 0 11px;font-size:9.3px;line-height:11.5px;color:#111}
.bubble{position:absolute;left:8px;top:42px;width:192px;height:78px;border:1px solid #ddd;background:#f7f7f7;font-size:9px;line-height:14.5px;color:#333;padding:8px 8px}
.bubble:after{content:"";position:absolute;left:130px;bottom:-20px;width:20px;height:20px;background:#f7f7f7;border-right:1px solid #ddd;clip-path:polygon(0 0,100% 0,100% 100%)}
.by{position:absolute;left:103px;top:146px;font-size:9.5px;line-height:14.5px;color:#222}
.avatar{position:absolute;left:171px;top:141px;width:27px;height:28px;background:linear-gradient(#6b5040,#c9a58a)}
.footer{left:0;top:1094px;width:960px;height:68px;background:var(--footer)}
.footer-bottom{left:0;top:1162px;width:960px;height:38px;background:var(--footer-dark)}
.foot-brand{left:86px;top:1106px;display:flex;align-items:center;gap:6px;font-family:Ubuntu,sans-serif;font-weight:500;font-size:15px;color:#ddd;letter-spacing:.5px}
.foot-brand span{width:40px;height:40px;border-radius:50%;background:#ddd}
.contact{right:88px;top:1103px;text-align:right;font-size:8.8px;color:#eee;line-height:17.5px}
.contact .gap{margin-top:5px}
.social{left:85px;top:1173px;display:flex;gap:16px}
.social span{width:17px;height:17px;background:#666;border-radius:2px}
.copy{right:92px;top:1175px;font-size:9.5px;color:#ddd}
</style>
</head>
<body>
<div class="page">
  <div class="abs top-band"></div>

  <nav class="abs nav">
    <a style="left:112px">Home</a>
    <a style="left:222px">Upcoming Auctions</a>
    <a class="active" style="left:357px">Auction Results</a>
    <a style="left:479px">Sell or Consign</a>
    <a style="left:586px">About Us</a>
    <a style="left:676px">Services</a>
    <a style="left:753px">FAQ</a>
    <a style="left:836px">Contact Us</a>
  </nav>
  <div class="abs dropdown">
    <div class="on">About Harwell</div>
    <div>Testimonials</div>
  </div>

  <div class="abs brand"><span class="brand-mark"></span><span class="brand-name">BRAMBLEWICK</span></div>

  <div class="abs phone">
    <span class="phone-icon"><svg width="12" height="12" viewBox="0 0 24 24"><path fill="#fff" d="M6.6 10.8a15 15 0 0 0 6.6 6.6l2.2-2.2c.3-.3.7-.4 1-.2 1.1.4 2.3.6 3.6.6.6 0 1 .4 1 1V20c0 .6-.4 1-1 1A17 17 0 0 1 3 4c0-.6.4-1 1-1h3.5c.6 0 1 .4 1 1 0 1.3.2 2.5.6 3.6.1.3 0 .7-.2 1z"/></svg></span>
    555-014-2290
  </div>

  <div class="abs frame"></div>
  <div class="abs slide" role="img" aria-label="Display case of graded coins in protective sleeves"></div>
  <form class="abs signup">
    <h2>Email sign-up form</h2>
    <p>Lorem ipsum dolor sit amet, consectetuer adipiscing elit. Nam</p>
    <div class="field">First Name</div>
    <div class="field">Last Name</div>
    <div class="field">Email Address</div>
    <div class="subscribe">Subscribe Now</div>
  </form>

  <svg class="abs arc" width="960" height="70" viewBox="0 0 960 70">
    <path d="M70 62 Q480 -30 896 62 Q480 8 70 62Z" fill="#fff"/>
    <path d="M70 62 Q480 -20 896 62 L896 70 L70 70Z" fill="#fff"/>
    <path d="M70 62 Q480 -38 896 62 Q480 -18 70 62Z" fill="#9b1a1e"/>
    <path d="M0 70 L70 62 Q480 -18 896 62 L960 70Z" fill="#fff"/>
  </svg>

  <div class="abs welcome"><span class="dot"></span>Welcome To <span class="name">BRAMBLEWICK</span><span class="dot"></span></div>

  <p class="abs intro"><b><i>simply dummy text of the printing and typesetting industry. Lorem Ipsum has been the industry's standard dummy text ever since the 1500s, when an</i></b> unknown printer took a galley of type and scrambled it to make a type speci men book. It has survived not only five centuries, but also a galley of type and scrambled &nbsp;the leap into electronic typesetting, remaining essen tially unchanged. It was popularised in the 1960s with the release of Letraset sheets containing Lorem Ipsum passages.<b>but also a galley of type and scrambled &nbsp;the leap into electronic</b> typesetting, remaining essen tially unchanged. It was popularised in the 1960s with the release of Letraset sheets containing Lorem Ipsum passages.but also a galley of type and scrambled &nbsp;the leap into electronic typesetting, remaining essen tially unchanged. It was popularised in the 1960s with the release of Letraset sheets containing ...</p>

  <div class="abs divider"></div>

  <section class="abs listings">
    <div class="head">Incredible Home in Fernhollow's exclusive Ridgewater community</div>
    <div class="row alt">
      <div class="thumb" role="img" aria-label="Stacked coins with a small figurine" style="background:linear-gradient(#8c8470,#c9c2b0)"></div>
      <div class="info"><div class="title">Live On-site Auction With Online Bidding</div><b>Begins:</b>&nbsp; Tuesday, April 23, 2013 at 10:00 AM EDT<br><br><b>Location:</b>&nbsp; Ridgewater Entrance- 1400 N. Lantern Hwy 9<br>Ridgewater Rd (Auction Property)<br>Fernhollow, NH 03201</div>
      <div class="btns"><div class="btn red"><i></i>Details</div><div class="btn blue"><i></i>Photos</div></div>
    </div>
    <div class="row">
      <div class="thumb" role="img" aria-label="Two gold coins" style="background:radial-gradient(circle at 40% 50%,#e2b84a,#8a5f14 70%,#2a2214);border:none"></div>
      <div class="info"><div class="title">Live On-site Auction With Online Bidding</div><b>Begins:</b>&nbsp; Tuesday, April 23, 2013 at 10:00 AM EDT<br><br><b>Location:</b>&nbsp; Ridgewater Entrance- 1400 N. Lantern Hwy 9<br>Ridgewater Rd (Auction Property)<br>Fernhollow, NH 03201</div>
      <div class="btns"><div class="btn red"><i></i>Details</div><div class="btn blue"><i></i>Photos</div></div>
    </div>
    <div class="row alt" style="border-bottom:none">
      <div class="thumb" role="img" aria-label="Two silver coins on black" style="background:radial-gradient(circle,#9a9a9a,#3a3a3a 55%,#050505 75%)"></div>
      <div class="info"><div class="title">Live On-site Auction With Online Bidding</div><b>Begins:</b>&nbsp; Tuesday, April 23, 2013 at 10:00 AM EDT<br><br><b>Location:</b>&nbsp; Ridgewater Entrance- 1400 N. Lantern Hwy 9<br>Ridgewater Rd (Auction Property)<br>Fernhollow, NH 03201</div>
      <div class="btns"><div class="btn red"><i></i>Details</div><div class="btn blue"><i></i>Photos</div></div>
    </div>
  </section>

  <aside class="abs side" style="top:680px">
    <div class="head">Featured Auction</div>
    <div class="featured-img" role="img" aria-label="Collectible coins for the featured auction"></div>
    <div class="feat-link">TRACTOR * HI LIFT * MACHINERY</div>
    <div class="feat-text"><b>Saturday</b> March 16, 2013 at 10:00 AM<br><span style="display:block;margin-top:4px">simply dummy text of the printing and typesetting industry.</span></div>
  </aside>

  <aside class="abs side" style="top:913px;height:175px">
    <div class="head">Client Testimonials</div>
    <div class="bubble">Simply dummy text of the printing and typesetting industry. Lorem Ipsum has been the industry's standard dummy text ever since the 1500s,</div>
    <div class="by">By<br>Delia Porwick</div>
    <div class="avatar" role="img" aria-label="Client portrait"></div>
  </aside>

  <footer>
    <div class="abs footer"></div>
    <div class="abs footer-bottom"></div>
    <div class="abs foot-brand"><span></span>BRAMBLEWICK</div>
    <div class="abs contact">Bramblewick Auctioneers<br>118 Quarry Lane • Ashmere, NH 03245<div class="gap">P: 555-014-7730 • F: 555-014-7731 • info@bramblewickbids.example</div></div>
    <div class="abs social"><span></span><span></span><span></span><span></span><span></span></div>
    <div class="abs copy">(C) 2013 The Bramblewick Auctioneers Companies</div>
  </footer>
</div>
</body>
</html>
```